Meadowlark Behavioral Partners, LLC Needs Modern Business Card Design.

We provide behavioral health services from western Kansas to eastern Kansas. There is an abundance of competition for the services we provide with our main competitor being larger and having significantly more financial resources; however, the quality of services we provide is greater and we have started to catch the attention of the State of Kansas. We had a great logo designed by PixelGuild - this will be used to build upon our brand. The logo (attached) should be used in the card development. We want something unique, modern, but also a card design that clearly states our name, contact info, provides the name and unqiue location of each clinician, etc. Rounded edges, or a unique size, just something that makes our business card stand out from others. I have also uploaded each clinician's name and their unique location and phone number.

Our idea is to have one side be black with our logo. Then, on the other side have business cards for each individual. Plus, we want one card that is "generic" with no specific clinician's name listed so that we can give clients an appointment card when they leave. Some clinicians have two locations - we're open to design and background color, but we have started going with branding colors of black, the yellow in the logo files attached, and sometimes a gray. Our new office has been decorated using this theme.

Target Market(s)

individuals and families in need of behavioral health services; potential professional referral sources; existing referral sources

Industry/Entity Type

Business

Contact Information for Business Card

I attached a Word doc that provides clinician names, credentials and location information specific to each individual.

Font styles to use
Serif

Colors
000000
fbed22
dbdbdb
9d9d9d
c3c3c3

Requirements
Must have
• 1) use of the company logo that has been attached; 2) a template that provides us space to individualize business cards for all of our clinicians; 3) should stick to the colors we are branding with: black, yellow from the logo file, maybe a gray shade and we're open to a suggestion on a shade of white.
Nice to have
• Group discussion culminated in the thought that one side would be black with just our logo - no clinician names, etc. A unique design - rounded edges, unique size, some catchy lay-out would be nice.
Should not have
• Must not be too busy. Should look "clean." The project should stick to branding colors: black, yellow (from the logo file), maybe a gray and shade of white.

```html
<!DOCTYPE html>
<html lang="en">
<head>
<meta charset="UTF-8">
<title>Meadowlark Behavioral Partners, LLC — Business Card</title>
<link rel="stylesheet" href="https://fonts.googleapis.com/css2?family=Cinzel:wght@600&family=Work+Sans:wght@400;600&display=swap">
<style>
  :root {
    --backdrop: #1f1f1f;
    --card-black: #1a1a1a;
    --card-black-soft: #262626;
    --brand-yellow: #fbbf1d;
    --brand-yellow-light: #fcd322;
    --brand-yellow-deep: #f7a81b;
    --text-white: #ffffff;
    --text-soft: #dbdbdb;
  }
  * { margin: 0; padding: 0; box-sizing: border-box; }
  html, body {
    width: 1200px;
    height: 900px;
    overflow: hidden;
    background: var(--backdrop);
  }
  .canvas {
    position: relative;
    width: 1200px;
    height: 900px;
  }
  .card {
    position: absolute;
    left: 250px;
    width: 700px;
    height: 400px;
    border-radius: 6px;
    overflow: hidden;
    background: linear-gradient(135deg, var(--card-black) 0%, var(--card-black-soft) 100%);
    box-shadow: 0 10px 30px rgba(0, 0, 0, 0.45);
  }
  .card--front { top: 40px; }
  .card--back  { top: 470px; }

  /* Front: company name */
  .company-name {
    position: absolute;
    inset: 0;
    display: flex;
    flex-direction: column;
    align-items: center;
    justify-content: center;
    font-family: "Cinzel", serif;
    font-weight: 600;
    color: var(--brand-yellow);
    text-align: center;
  }
  .company-name__primary {
    font-size: 54px;
    letter-spacing: 6px;
    line-height: 1.1;
  }
  .company-name__secondary {
    font-size: 22px;
    letter-spacing: 3px;
    margin-top: 6px;
  }

  /* Back: clinician details */
  .clinician {
    position: absolute;
    top: 46px;
    left: 46px;
    font-family: "Work Sans", sans-serif;
    color: var(--text-white);
  }
  .clinician__name {
    font-size: 22px;
    font-weight: 600;
    letter-spacing: 1.2px;
    text-transform: uppercase;
  }
  .clinician__title {
    font-size: 17px;
    font-weight: 400;
    letter-spacing: 1.2px;
    text-transform: uppercase;
    margin-top: 2px;
  }
  .clinician__phone {
    font-size: 16px;
    font-weight: 400;
    color: var(--text-soft);
    letter-spacing: 1px;
    margin-top: 20px;
  }
  .card__band {
    position: absolute;
    left: 0;
    bottom: 0;
    width: 700px;
    height: 400px;
  }
  .band-address {
    font-family: "Work Sans", sans-serif;
    font-size: 19px;
    fill: var(--text-white);
    letter-spacing: 0.6px;
  }
</style>
</head>
<body>
<main class="canvas">

  <section class="card card--front" aria-label="Card front">
    <div class="company-name">
      <span class="company-name__primary">MEADOWLARK</span>
      <span class="company-name__secondary">BEHAVIORAL PARTNERS, LLC</span>
    </div>
  </section>

  <section class="card card--back" aria-label="Card back">
    <div class="clinician">
      <p class="clinician__name">Daniel R. Hollis, LP</p>
      <p class="clinician__title">President</p>
      <p class="clinician__phone">(316) 555-0142</p>
    </div>

    <svg class="card__band" viewBox="0 0 700 400" aria-hidden="false">
      <defs>
        <linearGradient id="bandFill" x1="0" y1="0" x2="0" y2="1">
          <stop offset="0" stop-color="var(--brand-yellow-light)"/>
          <stop offset="1" stop-color="var(--brand-yellow-deep)"/>
        </linearGradient>
        <path id="addressCurve" d="M80,300 C240,284 420,306 600,360"/>
      </defs>
      <path d="M0,262 C200,232 450,252 700,368 L700,400 L0,400 Z" fill="url(#bandFill)"/>
      <text class="band-address">
        <textPath href="#addressCurve">418 N. Elm Ridge Ave Topeka, Kansas 66603</textPath>
      </text>
    </svg>
  </section>

</main>
</body>
</html>
```